KB Rubbish Removal Business Card

Hey,
I need a double sided business card designed for a rubbish removal business based in Australia. Logo is already chosen, similar colours preferred for both sides of the business card.

Details to include:

Front:

KB Rubbish Removal
Darren Holloway
Managing Director
Mobile: 0471 902 146
Email: darren@kbrubbishremoval.com.au
Website: kbrubbishremoval.com.au

Rear:

How did we do?
kbrubbishremoval.com.au/review

```html
<!DOCTYPE html>
<html lang="en">
<head>
<meta charset="utf-8">
<title>KB Rubbish Removal Business Card</title>
<link href="https://fonts.googleapis.com/css2?family=Roboto:wght@400;500&display=swap" rel="stylesheet">
<style>
  :root {
    --backdrop: #d9d9d9;
    --card-white: #ffffff;
    --brand-green: #0fcf58;
    --rule-green: #1ec34f;
    --icon-green: #22c15a;
    --text-grey: #4a4a4a;
    --gradient-light: #b3de3f;
    --gradient-dark: #2bbb46;
    --mark-green: #25b947;
  }
  * { margin: 0; padding: 0; box-sizing: border-box; }
  html, body {
    width: 1200px;
    height: 1200px;
    overflow: hidden;
    background: var(--backdrop);
    font-family: "Roboto", Arial, sans-serif;
  }
  .card {
    position: absolute;
    left: 219px;
    width: 763px;
    height: 437px;
  }
  .card-front { top: 115px; background: var(--card-white); }
  .card-back {
    top: 648px;
    background: linear-gradient(150deg, var(--gradient-light) 0%, var(--gradient-dark) 100%);
  }

  /* Front */
  .front-brand {
    position: absolute;
    left: 72px;
    top: 136px;
    width: 190px;
    text-align: center;
  }
  .front-brand .brand-dot {
    display: block;
    width: 100px;
    height: 100px;
    margin: 0 auto 16px;
    border-radius: 50%;
    background: var(--mark-green);
  }
  .front-brand .brand-name {
    font-size: 19px;
    font-weight: 500;
    color: var(--brand-green);
  }
  .divider {
    position: absolute;
    left: 310px;
    top: 121px;
    width: 1.5px;
    height: 201px;
    background: var(--rule-green);
  }
  .contact-block {
    position: absolute;
    left: 355px;
    top: 147px;
  }
  .person-name {
    font-size: 33px;
    font-weight: 500;
    letter-spacing: 0.5px;
    color: var(--brand-green);
    line-height: 1.1;
  }
  .person-title {
    font-size: 20px;
    color: var(--text-grey);
    margin-top: 1px;
  }
  .contact-list {
    list-style: none;
    margin-top: 14px;
  }
  .contact-list li {
    display: flex;
    align-items: center;
    font-size: 20.5px;
    color: var(--text-grey);
    height: 25px;
  }
  .contact-list svg {
    width: 13px;
    height: 13px;
    margin-right: 5px;
    flex: none;
  }

  /* Back */
  .back-brand {
    position: absolute;
    left: 116px;
    top: 160px;
    display: flex;
    align-items: center;
  }
  .back-brand .brand-dot {
    width: 88px;
    height: 88px;
    border-radius: 50%;
    background: var(--mark-green);
    margin-right: 20px;
  }
  .back-brand .brand-name {
    font-size: 41px;
    font-weight: 400;
    color: var(--card-white);
    letter-spacing: 0.3px;
  }
  .review-prompt {
    position: absolute;
    left: 224px;
    top: 268px;
    color: var(--card-white);
  }
  .review-question {
    font-size: 20px;
    font-weight: 500;
  }
  .review-link {
    font-size: 18px;
    margin-top: 4px;
  }
</style>
</head>
<body>
  <section class="card card-front">
    <div class="front-brand">
      <span class="brand-dot"></span>
      <span class="brand-name">KB Rubbish Removal</span>
    </div>
    <div class="divider"></div>
    <div class="contact-block">
      <h1 class="person-name">DARREN HOLLOWAY</h1>
      <p class="person-title">Managing Director</p>
      <ul class="contact-list">
        <li>
          <svg viewBox="0 0 16 16" aria-hidden="true"><path d="M4 1.5l2.2 3-1.3 1.6c.8 2 2.3 3.7 4.3 4.8l1.5-1.4 3 2.2-1.3 2.4C7.5 14 2.3 8.4 2 3.1z" fill="none" stroke="var(--icon-green)" stroke-width="1.6" stroke-linejoin="round"/></svg>
          0471 902 146
        </li>
        <li>
          <svg viewBox="0 0 16 16" aria-hidden="true"><rect x="1.5" y="3.5" width="13" height="9" fill="none" stroke="var(--icon-green)" stroke-width="1.5"/><path d="M1.5 3.5l6.5 5 6.5-5" fill="none" stroke="var(--icon-green)" stroke-width="1.5"/></svg>
          darren@kbrubbishremoval.com.au
        </li>
        <li>
          <svg viewBox="0 0 16 16" aria-hidden="true"><g fill="none" stroke="var(--icon-green)" stroke-width="1.2"><circle cx="8" cy="8" r="6.5"/><ellipse cx="8" cy="8" rx="3" ry="6.5"/><path d="M1.5 8h13M2.5 4.8h11M2.5 11.2h11"/></g></svg>
          www.kbrubbishremoval.com.au
        </li>
      </ul>
    </div>
  </section>

  <section class="card card-back">
    <div class="back-brand">
      <span class="brand-dot"></span>
      <span class="brand-name">KB RUBBISH REMOVAL</span>
    </div>
    <div class="review-prompt">
      <p class="review-question">How did we do?</p>
      <p class="review-link">kbrubbishremoval.com.au/review</p>
    </div>
  </section>
</body>
</html>
```